Velmira Body Oil Label for 4 -8 oz bottles

We are selling 4 and 8 oz body oils and need a label to put on our bottles. I'm not sure if we want a label for the front and also the back of the bottle or just one label in the front. You can give me examples of each way. Attached is our logo on a blue background but the background will change colors depending on the scent as specified in the design description. Our bottle will be either clear or white with a pump spray type lid as shown in the attached example. Attached are also our design criteria which is needed for the labels.
Updates

We have decided to use the disc top cap and not the pump spray cap. If you are able to, please show us the design on the 4 oz bottle with the disc top cap. Thanks

Target Market(s)

women

Industry/Entity Type

skincare, cosmetics

Font styles to use
Serif
Sans Serif

Requirements
Must have
• stylish name for each scented oil which contrasts the font in the logo. Also must have darker colors since the logo colors are lighter.
Nice to have
• Border around the labels, maybe one solid color or maybe two complimenting colors which go well with the fragrnace name
Should not have
• background colors that match the logo colors

```html
<!DOCTYPE html>
<html lang="en">
<head>
<meta charset="utf-8">
<title>Velmira Body Oil Labels</title>
<link rel="stylesheet" href="https://fonts.googleapis.com/css2?family=Playfair+Display:wght@400;800&family=Raleway:wght@300;400&family=Montserrat:wght@600&display=swap">
<style>
  :root {
    --canvas: #f4f4f4;
    --white: #ffffff;
    --candy-drop: #f98ba1;
    --candy-side: #a9dcfb;
    --lavender-drop: #a96dc9;
    --lavender-side: #dcc2ea;
    --canopy-drop: #2a3a17;
    --canopy-side: #bdd495;
    --fruity-drop: #fd9a39;
    --fruity-side: #fdd1a3;
  }
  * { margin: 0; padding: 0; box-sizing: border-box; }
  html, body {
    width: 1200px; height: 675px; overflow: hidden;
    background: var(--canvas);
  }
  .label-row {
    width: 1200px; height: 675px;
    display: flex; align-items: center; justify-content: center;
    gap: 67px;
  }
  .label {
    position: relative;
    width: 233px; height: 560px;
    border-radius: 14px;
    overflow: hidden;
    background: var(--side);
    color: var(--white);
    text-align: center;
  }
  .label--candy { --side: var(--candy-side); --drop: var(--candy-drop); }
  .label--lavender { --side: var(--lavender-side); --drop: var(--lavender-drop); }
  .label--canopy { --side: var(--canopy-side); --drop: var(--canopy-drop); }
  .label--fruity { --side: var(--fruity-side); --drop: var(--fruity-drop); }
  .label__drop { position: absolute; inset: 0; width: 100%; height: 100%; }
  .label__drop path { fill: var(--drop); }
  .label__sheen {
    position: absolute; inset: 0;
    background: linear-gradient(90deg, rgba(255,255,255,0.18) 0%, rgba(255,255,255,0) 22%, rgba(255,255,255,0) 70%, rgba(255,255,255,0.22) 85%, rgba(255,255,255,0) 100%);
  }
  .label__brand {
    position: absolute; left: 0; right: 0; top: 112px;
  }
  .brand__name {
    font-family: "Playfair Display", serif;
    font-weight: 400; font-size: 38px; line-height: 40px;
    letter-spacing: 1px;
  }
  .brand__tag {
    font-family: "Raleway", sans-serif;
    font-weight: 400; font-size: 9px; letter-spacing: 2.5px;
    margin-top: 2px;
  }
  .label__scent {
    position: absolute; left: 6px; right: 6px; top: 206px; height: 110px;
    display: flex; flex-direction: column; justify-content: center;
    font-family: "Playfair Display", serif;
    font-weight: 800; font-size: 46px; line-height: 44px;
    letter-spacing: -0.5px;
  }
  .label--canopy .label__scent { font-size: 40px; line-height: 42px; }
  .label__type {
    position: absolute; left: 36px; width: 162px; top: 334px; height: 23px;
    background: var(--white);
    color: var(--drop);
    font-family: "Raleway", sans-serif;
    font-weight: 400; font-size: 19px; line-height: 23px;
  }
  .label__claims {
    position: absolute; left: 20px; right: 20px; top: 422px;
    font-family: "Montserrat", sans-serif;
    font-weight: 600; font-size: 10px; letter-spacing: 0.3px;
  }
  .claims__row {
    display: flex; justify-content: center;
    border-bottom: 1.5px solid var(--white);
    padding-bottom: 1px;
  }
  .claims__row span { padding: 2px 4px 0; }
  .claims__row span + span { border-left: 1.5px solid var(--white); }
  .claims__main { margin-top: 5px; }
  .label__size {
    position: absolute; left: 0; right: 0; top: 519px;
    font-family: "Raleway", sans-serif; font-weight: 400; font-size: 10px;
  }
</style>
</head>
<body>
<main class="label-row">

  <article class="label label--candy">
    <svg class="label__drop" viewBox="0 0 233 560" aria-hidden="true"><path d="M116.5 0 L233 210 L233 494 Q233 560 116.5 560 Q0 560 0 494 L0 210 Z"/></svg>
    <div class="label__sheen"></div>
    <div class="label__brand"><div class="brand__name">Velmira</div><div class="brand__tag">BODY OILS</div></div>
    <h2 class="label__scent"><span>Cotton</span><span>Candy</span></h2>
    <div class="label__type">BODY OIL</div>
    <div class="label__claims"><div class="claims__row"><span>NON-GREESY</span><span>WITH VITAMIN E</span></div><div class="claims__main">ULTRA MOISTURIZING</div></div>
    <div class="label__size">4OZ</div>
  </article>

  <article class="label label--lavender">
    <svg class="label__drop" viewBox="0 0 233 560" aria-hidden="true"><path d="M116.5 0 L233 210 L233 494 Q233 560 116.5 560 Q0 560 0 494 L0 210 Z"/></svg>
    <div class="label__sheen"></div>
    <div class="label__brand"><div class="brand__name">Velmira</div><div class="brand__tag">BODY OILS</div></div>
    <h2 class="label__scent" style="top:218px"><span>Soft</span><span>Lavender</span></h2>
    <div class="label__type">BODY OIL</div>
    <div class="label__claims"><div class="claims__row"><span>NON-GREESY</span><span>WITH VITAMIN E</span></div><div class="claims__main">ULTRA MOISTURIZING</div></div>
    <div class="label__size">4OZ</div>
  </article>

  <article class="label label--canopy">
    <svg class="label__drop" viewBox="0 0 233 560" aria-hidden="true"><path d="M116.5 0 L233 210 L233 494 Q233 560 116.5 560 Q0 560 0 494 L0 210 Z"/></svg>
    <div class="label__sheen"></div>
    <div class="label__brand"><div class="brand__name">Velmira</div><div class="brand__tag">BODY OILS</div></div>
    <h2 class="label__scent" style="top:218px"><span>Wild Canopy</span></h2>
    <div class="label__type">BODY OIL</div>
    <div class="label__claims"><div class="claims__row"><span>NON-GREESY</span><span>WITH VITAMIN E</span></div><div class="claims__main">ULTRA MOISTURIZING</div></div>
    <div class="label__size">4OZ</div>
  </article>

  <article class="label label--fruity">
    <svg class="label__drop" viewBox="0 0 233 560" aria-hidden="true"><path d="M116.5 0 L233 210 L233 494 Q233 560 116.5 560 Q0 560 0 494 L0 210 Z"/></svg>
    <div class="label__sheen"></div>
    <div class="label__brand"><div class="brand__name">Velmira</div><div class="brand__tag">BODY OILS</div></div>
    <h2 class="label__scent"><span>Fruity</span><span>Delights</span></h2>
    <div class="label__type">BODY OIL</div>
    <div class="label__claims"><div class="claims__row"><span>NON-GREESY</span><span>WITH VITAMIN E</span></div><div class="claims__main">ULTRA MOISTURIZING</div></div>
    <div class="label__size">4OZ</div>
  </article>

</main>
</body>
</html>
```